Hacienda Vista Moreno Business cards

We would like 3 individual business cards with the logo you designed:

1) Dana Perlwitz - Phone: 206 417 6093
2) Theodore M Perlwitz - Phone 206 581 2746
3) Marta Bylund - Phone 310-864-2071

Address for all three cards:
7128 284th Ave NE
Birchmont, OR 97420
HaciendaVistaMoreno@mailbrook.net

Industry/Entity Type

Business

```html
<!DOCTYPE html>
<html lang="en">
<head>
<meta charset="utf-8">
<title>Hacienda Vista Moreno – Business Cards</title>
<link rel="stylesheet" href="https://fonts.googleapis.com/css2?family=Questrial&family=Nanum+Pen+Script&display=swap">
<style>
  :root {
    --page: #ffffff;
    --ink: #141414;
    --card-lime: #d6df22;
    --card-green: #c0d83e;
    --card-grey: #d3d5d4;
    --card-grey-edge: #a9c98e;
    --frame: #ffffff;
    --art-dark: #1e1e1e;
    --art-mid: #3a3a3a;
  }
  * { margin: 0; padding: 0; box-sizing: border-box; }
  html, body {
    width: 1200px; height: 782px; overflow: hidden;
    background: var(--page);
  }
  .sheet { position: relative; width: 1200px; height: 782px; }

  .card {
    position: absolute;
    width: 576px; height: 372px;
    color: var(--ink);
    font-family: "Questrial", "Century Gothic", sans-serif;
    text-align: center;
  }
  .card--dana { left: 3px; top: 3px; background: var(--card-lime); }
  .card--theo { left: 621px; top: 3px; background: var(--card-green); }
  .card--marta { left: 316px; top: 406px; background: var(--card-grey); outline: 1px solid var(--card-grey-edge); }

  .card__frame {
    position: absolute; inset: 16px;
    border: 1px solid var(--frame);
  }
  .card__art {
    position: absolute; left: 205px; top: 32px;
    width: 166px; height: 96px;
  }
  .card__brand {
    position: absolute; left: 0; right: 0; top: 144px;
    font-size: 29px; letter-spacing: 0.5px;
    text-transform: uppercase;
    line-height: 1;
  }
  .card__name {
    position: absolute; left: 0; right: 0; top: 218px;
    font-family: "Nanum Pen Script", cursive;
    font-size: 42px; line-height: 1;
  }
  .card__contact {
    position: absolute; left: 0; right: 0; top: 293px;
    font-size: 19px; line-height: 22px;
    display: flex; justify-content: center; align-items: center; gap: 7px;
  }
  .card__phone-icon { width: 17px; height: 17px; }
  .card__divider {
    width: 4px; height: 22px; background: var(--frame);
    margin: 0 3px;
  }
  .card__address {
    position: absolute; left: 0; right: 0; top: 323px;
    font-size: 19px; line-height: 22px;
  }
</style>
</head>
<body>
<main class="sheet">

  <article class="card card--dana">
    <div class="card__frame"></div>
    <svg class="card__art" role="img" aria-label="Ranch illustration: oak tree, fence, horses and birds" viewBox="0 0 166 96">
      <defs><linearGradient id="art1" x1="0" y1="0" x2="1" y2="1"><stop offset="0" stop-color="#1e1e1e"/><stop offset="1" stop-color="#3a3a3a"/></linearGradient></defs>
      <rect width="166" height="96" rx="6" fill="url(#art1)"/>
    </svg>
    <div class="card__brand">Hacienda Vista Moreno</div>
    <div class="card__name">Dana Perlwitz</div>
    <div class="card__contact">
      <svg class="card__phone-icon" viewBox="0 0 16 16" aria-hidden="true"><circle cx="8" cy="8" r="7" fill="none" stroke="currentColor" stroke-width="1.4"/><path d="M6 4.2c-.8.5-1.2 1.4-1 2.5.3 2 1.7 4 3.6 4.9 1 .4 1.9.3 2.5-.4l-1.4-1.5-1 .5c-.8-.5-1.5-1.5-1.7-2.4l.8-.7z" fill="currentColor"/></svg>
      <span class="card__phone">206 417 6093</span>
      <span class="card__divider"></span>
      <span class="card__email">haciendavistamoreno@mailbrook.net</span>
    </div>
    <div class="card__address">7128 284th Ave NE Birchmont, OR 97420</div>
  </article>

  <article class="card card--theo">
    <div class="card__frame"></div>
    <svg class="card__art" role="img" aria-label="Ranch illustration: oak tree, fence, horses and birds" viewBox="0 0 166 96">
      <defs><linearGradient id="art2" x1="0" y1="0" x2="1" y2="1"><stop offset="0" stop-color="#1e1e1e"/><stop offset="1" stop-color="#3a3a3a"/></linearGradient></defs>
      <rect width="166" height="96" rx="6" fill="url(#art2)"/>
    </svg>
    <div class="card__brand">Hacienda Vista Moreno</div>
    <div class="card__name">Theodore M Perlwitz</div>
    <div class="card__contact">
      <svg class="card__phone-icon" viewBox="0 0 16 16" aria-hidden="true"><circle cx="8" cy="8" r="7" fill="none" stroke="currentColor" stroke-width="1.4"/><path d="M6 4.2c-.8.5-1.2 1.4-1 2.5.3 2 1.7 4 3.6 4.9 1 .4 1.9.3 2.5-.4l-1.4-1.5-1 .5c-.8-.5-1.5-1.5-1.7-2.4l.8-.7z" fill="currentColor"/></svg>
      <span class="card__phone">206 581 2746</span>
      <span class="card__divider"></span>
      <span class="card__email">haciendavistamoreno@mailbrook.net</span>
    </div>
    <div class="card__address">7128 284th Ave NE Birchmont, OR 97420</div>
  </article>

  <article class="card card--marta">
    <div class="card__frame"></div>
    <svg class="card__art" role="img" aria-label="Ranch illustration: oak tree, fence, horses and birds" viewBox="0 0 166 96">
      <defs><linearGradient id="art3" x1="0" y1="0" x2="1" y2="1"><stop offset="0" stop-color="#1e1e1e"/><stop offset="1" stop-color="#3a3a3a"/></linearGradient></defs>
      <rect width="166" height="96" rx="6" fill="url(#art3)"/>
    </svg>
    <div class="card__brand">Hacienda Vista Moreno</div>
    <div class="card__name">Marta Bylund</div>
    <div class="card__contact">
      <svg class="card__phone-icon" viewBox="0 0 16 16" aria-hidden="true"><circle cx="8" cy="8" r="7" fill="none" stroke="currentColor" stroke-width="1.4"/><path d="M6 4.2c-.8.5-1.2 1.4-1 2.5.3 2 1.7 4 3.6 4.9 1 .4 1.9.3 2.5-.4l-1.4-1.5-1 .5c-.8-.5-1.5-1.5-1.7-2.4l.8-.7z" fill="currentColor"/></svg>
      <span class="card__phone">310 864 2071</span>
      <span class="card__divider"></span>
      <span class="card__email">haciendavistamoreno@mailbrook.net</span>
    </div>
    <div class="card__address">7128 284th Ave NE Birchmont, OR 97420</div>
  </article>

</main>
</body>
</html>
```